integrative health clinic-Medical massage, acupuncture, chiropractic

we like our logo, but are open to new ideas. We need a new card design. We have added chiropractic and acupuncture that we have put under the name of the business. We are an integrative medical clinic

Target Market(s)

General public, athletes

Contact Information for Business Card

Phone 5055583927
Fax 5055583926
Hours Monday-Friday 9-6
Saturday 10-6
The 20% can be smaller on the back

Colors
3176b5
0355a3

Requirements
Must have
• Logo but am open to ideas
Nice to have
• We are an integrated medical clinic but also want to be personable. We want the card fun and inviting

```html
<!DOCTYPE html>
<html lang="en">
<head>
<meta charset="utf-8">
<title>Juniper Motion Clinic — Business Card</title>
<link href="https://fonts.googleapis.com/css2?family=Montserrat:wght@700;800&family=Questrial&display=swap" rel="stylesheet">
<style>
  :root {
    --bg: #2b2f35;
    --card: #ffffff;
    --ink: #111111;
    --blue: #0355a3;
    --blue-soft: #3176b5;
    --rule: #222222;
  }
  * { box-sizing: border-box; margin: 0; padding: 0; }
  html, body { width: 1200px; height: 900px; overflow: hidden; background: var(--bg); }
  .canvas {
    width: 1200px; height: 900px;
    display: flex; align-items: center; justify-content: center; gap: 40px;
  }
  .card {
    width: 560px; height: 320px; background: var(--card);
    position: relative; overflow: hidden;
    box-shadow: 0 6px 18px rgba(0,0,0,.35);
  }

  /* business name, set as plain text */
  .business-name {
    position: absolute;
    font-family: 'Montserrat', sans-serif; font-weight: 700; color: var(--ink);
    line-height: 1; white-space: nowrap;
  }

  /* contact side */
  .contact .business-name {
    top: 36px; left: 206px; font-size: 24px;
    padding-bottom: 10px; border-bottom: 1px solid var(--rule);
  }
  .contact-lines {
    position: absolute; top: 30px; left: 22px; width: 176px;
    font-family: 'Questrial', sans-serif; font-size: 14px; color: var(--ink); line-height: 1.35;
  }
  .contact-lines .num { font-family: 'Montserrat', sans-serif; font-weight: 800; font-size: 14px; }
  .contact-lines .hours { color: var(--blue); }
  .contact-lines .hours span { display: block; padding-left: 58px; }
  .divider { position: absolute; left: 200px; top: 120px; width: 1px; height: 90px; background: var(--rule); }
  .services {
    position: absolute; top: 128px; left: 218px; list-style: none;
    font-family: 'Montserrat', sans-serif; font-weight: 800; font-size: 17px; color: var(--blue); line-height: 1.2;
  }
  .services li::before { content: "•"; margin-right: 6px; }
  .contact-foot {
    position: absolute; left: 22px; bottom: 22px;
    font-family: 'Questrial', sans-serif; font-size: 19px; color: var(--ink); line-height: 1.35;
  }
  .contact-foot .label { display: inline-block; width: 82px; }

  /* booking side */
  .headline {
    position: absolute; top: 16px; left: 20px; right: 20px;
    display: flex; align-items: center; gap: 10px;
    font-family: 'Montserrat', sans-serif; font-weight: 800; font-size: 56px; color: var(--blue); line-height: 1;
  }
  .headline .bar { flex: 1; height: 3px; background: var(--blue); }
  .url {
    position: absolute; top: 84px; left: 0; right: 0; text-align: center;
    font-family: 'Questrial', sans-serif; font-size: 27px; color: var(--blue-soft);
  }
  .offer {
    position: absolute; top: 138px; left: 26px; width: 200px; height: 52px;
    display: flex; align-items: center; gap: 4px;
    font-family: 'Montserrat', sans-serif; color: var(--ink);
  }
  .offer svg { position: absolute; inset: 0; }
  .offer .pct { font-weight: 800; font-size: 26px; margin-left: 14px; }
  .offer .txt { font-weight: 700; font-size: 12px; letter-spacing: .3px; }
  .offer-arrow { position: absolute; top: 170px; left: 232px; font-family: 'Montserrat', sans-serif; font-weight: 800; color: var(--blue); font-size: 14px; }
  .booking .business-name { top: 156px; left: 258px; font-size: 20px; }
  .social { position: absolute; top: 208px; left: 26px; width: 34px; height: 34px; border-radius: 6px; background: var(--blue-soft); }
  .insurance {
    position: absolute; top: 212px; left: 70px; right: 20px;
    font-family: 'Montserrat', sans-serif; font-weight: 800; font-size: 19px; color: var(--blue); line-height: 1.35;
  }
</style>
</head>
<body>
<main class="canvas">

  <section class="card contact">
    <div class="contact-lines">
      <div>Phone: <span class="num">(505) 558 3927</span></div>
      <div>Fax: <span class="num" style="margin-left:26px">(505) 558 3926</span></div>
      <div class="hours">Hours Monday-Friday 9-6<span>Saturday 10-6</span></div>
    </div>
    <div class="business-name">Juniper Motion Clinic</div>
    <div class="divider"></div>
    <ul class="services">
      <li>Specializing In Medical</li>
      <li>Sports Massage</li>
      <li>Manual Therapies</li>
      <li>Chiropractic</li>
      <li>Acupuncture</li>
    </ul>
    <div class="contact-foot">
      <div><span class="label">Email:</span>info@junipermotionnm.com</div>
      <div>Address: 418 Cerrillos, B3 Santa Fe, NM 87505</div>
    </div>
  </section>

  <section class="card booking">
    <h1 class="headline"><span class="bar"></span>Book Online<span class="bar"></span></h1>
    <div class="url">www.junipermotionnm.com</div>
    <div class="offer">
      <svg width="200" height="52" viewBox="0 0 200 52" aria-hidden="true">
        <polyline points="30,2 2,2 2,24" fill="none" stroke="#111" stroke-width="2"/>
        <polyline points="170,50 198,50 198,28" fill="none" stroke="#111" stroke-width="2"/>
      </svg>
      <span class="pct">20%</span><span class="txt">OFF FIRST VISIT</span>
    </div>
    <span class="offer-arrow">»</span>
    <div class="business-name">Juniper Motion Clinic</div>
    <span class="social"></span>
    <p class="insurance">We Accept Some Insurances,<br>Worker's Comp And Personal Injury.</p>
  </section>

</main>
</body>
</html>
```